Web Design Job: Facial Surgery Center (Velantra)--Web Design Needed

We need a web design for Velantra Facial Surgery. Velantra is in Chesterfield, MO (suburb of St. Louis), and is owned by a double board certified facial plastic surgeon and ENT. The website must feature a before and after photo book, a section for patient reviews, drop down menus that outline services offered (one for surgical procedures and one for office/nonsurgical procedures), and "About the Practice" section, a section to talk about the doctor and his staff, a "What's New" section, a section for information for out of town patients, as well as a link to the Medical Spa also owned by the doctor, as well as Facefeed and Chirper. We are open to ideas regarding adding a "tour of the surgery center", featuring video footage of the state of the art facility, as well as other video options. We prefer soothing colors such as aquas and blues, light greys, chocolate browns, etc (does not have to follow the color scheme in the attached logo). We would like the design to be easy to digest and informative, but not "thick". It should be an upscale, classy design that will appeal to all age brackets, but especially middle-aged women, as that is the primary clientele.

Target Market(s)

Middle aged women are our most common client, however, younger patients, both male and female, will often visit the site for select procedures.

Industry/Entity Type

Medical

Number of Pages Required

5+ page

Font styles to use
Sans Serif

Colors
86cfc6
85cae6
cee9f5
cfeae6
edf8f6
85acd3
cfdfed

Requirements
Must have
• Before and after picture book, links to Facefeed, Chirper and Instagram, a soothing, peaceful aesthetic, a page for reviews, as well as a link to reviews on Yelp or similar page.
Nice to have
• Drop down menus that include the surgical and nonsurgical procedures. Each surgical procedure could have it's own section that includes a before and after picture book.
Should not have
• Too many words!

```html
<!DOCTYPE html>
<html lang="en">
<head>
<meta charset="utf-8">
<title>Velantra Facial Surgery</title>
<link href="https://fonts.googleapis.com/css2?family=Open+Sans:wght@400;600;700;800&display=swap" rel="stylesheet">
<style>
:root{
  --navy:#1d5a9c;
  --navy-dark:#163f70;
  --blue:#2a78b8;
  --teal:#1cb5b8;
  --teal-light:#86cfc6;
  --aqua-pale:#cee9f5;
  --grey-bg:#eef0f2;
  --grey-text:#6b7077;
  --ink:#2c3440;
  --white:#ffffff;
  --skin:#d9b59c;
  --skin-light:#efd9c8;
}
*{box-sizing:border-box;margin:0;padding:0}
html,body{width:1200px;height:5000px;overflow:hidden}
body{font-family:'Open Sans',Arial,sans-serif;color:var(--ink);background:var(--white);position:relative}
section,header,nav,footer{position:relative;width:1200px;overflow:hidden}
.abs{position:absolute}
.ph{position:absolute}
.lorem{font-size:15px;line-height:23px;color:var(--grey-text)}
.section-title{font-size:27px;font-weight:700;text-transform:uppercase;color:var(--navy);letter-spacing:.3px}
.section-title .accent{color:var(--teal)}
.btn{display:inline-block;font-size:14px;font-weight:700;color:var(--white);background:var(--navy);padding:9px 28px;text-transform:uppercase;letter-spacing:.5px}

/* header */
.site-header{height:127px}
.header-address{left:40px;top:38px;display:flex;gap:12px;align-items:flex-start}
.header-address p{font-size:15px;font-weight:700;line-height:20px;color:var(--ink)}
.brand{left:0;width:1200px;top:40px;text-align:center;font-size:32px;font-weight:600;color:var(--navy)}
.header-phone{right:40px;top:40px;display:flex;gap:12px;align-items:center}
.header-phone small{display:block;font-size:11px;font-weight:700;color:var(--ink)}
.header-phone strong{display:block;font-size:26px;font-weight:700;color:var(--ink);line-height:28px}

/* nav */
.main-nav{height:46px;background:var(--teal);display:flex;align-items:stretch;padding-left:20px}
.main-nav a{display:flex;align-items:center;padding:0 13px;font-size:13.5px;font-weight:700;color:var(--white);text-transform:uppercase;text-decoration:none}
.main-nav a.active{background:var(--navy)}

/* hero */
.hero{height:560px;background:#20262c}
.hero-photo{left:0;top:0;width:1200px;height:552px;background:radial-gradient(ellipse 420px 460px at 600px 260px,#c9a38d 0%,#8a6654 45%,#3a3431 80%,#1e2226 100%)}
.hero-title{left:0;width:1200px;top:150px;text-align:center;font-size:44px;font-weight:800;text-transform:uppercase;color:#7fe0d8;letter-spacing:1px}
.hero-sub{left:0;width:1200px;top:208px;text-align:center;font-size:24px;font-weight:600;color:var(--white)}
.play{left:530px;top:278px}
.hero-strip{left:0;bottom:0;width:1200px;height:8px;background:var(--teal)}
.hero-strip span{position:absolute;right:40px;top:0;width:170px;height:8px;background:var(--navy)}

/* welcome */
.welcome{height:167px;text-align:center}
.welcome h1{position:absolute;left:0;width:1200px;top:34px;font-size:27px;font-weight:700;color:var(--navy)}
.welcome p{position:absolute;left:60px;width:1080px;top:82px}

/* facial procedures */
.facial{height:383px;background:linear-gradient(90deg,var(--navy-dark) 0%,var(--navy) 45%,var(--blue) 100%)}
.facial-photo{left:0;top:0;width:390px;height:383px;background:linear-gradient(160deg,#e9e4df 0%,#d7c1b0 50%,#c9a890 100%)}
.facial .section-title{right:90px;top:36px;color:var(--white)}
.facial .lorem{left:420px;width:700px;top:84px;color:var(--white);text-align:right}
.facial .card{top:148px;width:330px;height:198px}
.arrow{font-size:40px;font-weight:400;line-height:40px}
.facial .arrow{color:var(--white);top:220px}

.card{position:absolute;background:var(--white);border:3px solid var(--white)}
.card .img{position:absolute;left:0;top:0;right:0;bottom:36px}
.card .label{position:absolute;left:0;right:0;bottom:0;height:36px;display:flex;align-items:center;justify-content:space-between;padding:0 10px 0 14px;font-size:14px;font-weight:700;text-transform:uppercase;color:var(--navy);background:var(--white)}
.card .plus{width:20px;height:20px;border-radius:50%;background:var(--grey-text);color:var(--white);font-size:16px;line-height:20px;text-align:center;font-weight:700}

/* office */
.office{height:494px}
.office .section-title{left:0;width:1200px;top:34px;text-align:center}
.office .lorem{left:90px;width:1020px;top:80px;text-align:center}
.office .card{top:212px;width:338px;height:222px;border:none}
.office .card .label{background:var(--teal);color:var(--white)}
.office .card .plus{background:var(--white);color:var(--teal)}
.office .arrow{color:#9aa1a8;top:290px}

/* about */
.about{height:646px;background:var(--grey-bg)}
.doctor-photo{left:30px;top:0;width:340px;height:646px;background:linear-gradient(180deg,#e9e9ea 0%,#f6f6f6 20%,#e3e6ea 100%)}
.about-title{left:470px;top:34px}
.about .lorem.bio{left:470px;width:700px;top:80px}
.about .btn.more{left:470px;top:230px;position:absolute}
.team-title{left:470px;top:318px}
.member{position:absolute;top:360px;width:200px;text-align:center}
.member .avatar{width:200px;height:200px;border-radius:50%;border:6px solid var(--white);background:radial-gradient(circle at 50% 45%,#e7d3c4 0%,#cfb39f 55%,#b79b88 100%);box-shadow:0 2px 6px rgba(0,0,0,.12)}
.member h3{font-size:16px;font-weight:700;color:var(--ink);margin-top:12px}
.member p{font-size:14px;color:var(--teal);font-weight:600}

/* out of town */
.spacer{height:50px}
.out-town{height:267px;background:linear-gradient(90deg,var(--blue) 0%,#3f8ec6 50%,var(--navy) 100%)}
.out-town .backdrop{left:0;top:0;width:1200px;height:267px;background:linear-gradient(90deg,rgba(255,255,255,.08),rgba(133,202,230,.25),rgba(255,255,255,.05))}
.out-town .section-title{left:0;width:1200px;top:30px;text-align:center;color:var(--white)}
.out-town .lorem{left:90px;width:1020px;top:76px;text-align:center;color:var(--white)}
.out-town .btn{position:absolute;left:530px;top:196px;background:var(--teal)}

/* gallery */
.gallery{height:610px}
.gallery .section-title{left:72px;top:22px}
.filter{right:70px;top:26px;width:200px;height:32px;background:var(--navy);color:var(--white);font-size:14px;font-weight:700;display:flex;align-items:center;justify-content:space-between;padding:0 12px}
.gallery-grid{left:0;top:93px;width:1200px;height:517px;display:grid;grid-template-columns:repeat(3,1fr);grid-template-rows:repeat(2,1fr);gap:3px}
.gallery-grid div{position:relative}

/* social */
.social{height:550px}
.social .section-title{left:0;width:1200px;top:30px;text-align:center}
.widget{position:absolute;top:84px;height:433px;background:var(--white);border:1px solid #d4d8dc;box-shadow:0 1px 4px rgba(0,0,0,.08)}
.fb-widget{left:230px;width:410px}
.fb-cover{left:10px;top:10px;width:388px;height:96px;background:linear-gradient(90deg,#7f98b8,#c7b3a6)}
.fb-name{left:24px;top:22px;font-size:15px;font-weight:700;color:var(--white)}
.fb-like{left:24px;top:72px;display:flex;gap:6px}
.fb-like span{font-size:11px;font-weight:700;background:var(--white);color:var(--ink);padding:2px 8px;border:1px solid #ccc}
.fb-friends{left:10px;top:116px;width:388px;font-size:11px;color:var(--grey-text)}
.fb-faces{left:10px;top:136px;display:flex;gap:4px}
.fb-faces span{width:30px;height:30px;background:#c5b7ad}
.fb-post{left:10px;top:182px;width:388px;border-top:1px solid #e2e5e8;padding-top:12px}
.fb-post .who{display:flex;gap:8px;align-items:center;font-size:12px;font-weight:700;color:var(--navy)}
.fb-post .who span{width:32px;height:32px;background:var(--aqua-pale)}
.fb-post p{font-size:12px;line-height:18px;color:var(--grey-text);margin-top:8px;width:200px}
.fb-post .thumb{position:absolute;right:0;top:56px;width:170px;height:150px;background:linear-gradient(150deg,#e2d2c6,#bfa493)}
.tw-widget{left:652px;width:320px}
.tw-head{left:0;top:0;width:318px;height:42px;border-bottom:1px solid #e2e5e8;display:flex;align-items:center;justify-content:space-between;padding:0 12px}
.tw-head b{font-size:13px;color:var(--ink)}
.tw-head span{font-size:11px;font-weight:600;border:1px solid #bfc5cb;padding:3px 8px;color:var(--ink);display:flex;gap:5px;align-items:center}
.tweet{position:absolute;left:0;width:318px;padding:0 12px 0 52px}
.tweet::before{content:"";position:absolute;left:12px;top:2px;width:30px;height:30px;background:var(--aqua-pale)}
.tweet small{display:block;font-size:10px;color:#9aa1a8}
.tweet p{font-size:11px;line-height:16px;color:var(--grey-text)}
.tw-foot{left:12px;bottom:12px;width:294px;height:28px;border:1px solid #d4d8dc;font-size:11px;color:#9aa1a8;padding:6px 8px}

/* testimonials */
.testimonials{height:317px;background:var(--navy)}
.testimonials .section-title{left:0;width:1200px;top:28px;text-align:center;color:var(--teal)}
.quote-avatar{left:120px;top:92px;width:110px;height:110px;border-radius:50%;border:5px solid var(--white);background:radial-gradient(circle at 50% 45%,#e8d0bd,#b99682)}
.bubble-tip{left:226px;top:138px}
.quote-mark{font-size:90px;font-weight:800;color:var(--teal);line-height:90px}
.testimonials .lorem{left:340px;width:720px;top:102px;color:var(--white);font-size:16px;line-height:25px}
.testimonials .name{left:340px;top:188px;font-size:20px;font-weight:700;color:var(--white)}
.dots{left:572px;top:262px;display:flex;gap:8px}
.dots span{width:12px;height:12px;border-radius:50%;border:2px solid var(--white)}
.dots span.on{background:var(--white)}

/* booking */
.booking{height:433px}
.booking .section-title{left:72px;top:32px;font-size:24px;color:var(--ink)}
.form{left:72px;top:86px;width:376px}
.form .row{display:flex;gap:10px;margin-bottom:10px}
.field{flex:1;height:32px;border:1px solid #cfd4d9;background:#f7f8f9;font-size:12px;color:var(--grey-text);padding:7px 10px;display:flex;justify-content:space-between}
.field.area{height:126px}
.form .btn{margin-top:12px;margin-left:110px;padding:8px 60px;background:var(--blue);font-size:13px}
.map{left:470px;top:0;width:730px;height:433px;background:linear-gradient(135deg,#e8ecef 0%,#f3f1e7 45%,#e1e6ea 100%)}

/* footer */
.site-footer{height:313px;background:var(--navy)}
.footer-white{right:0;top:0}
.footer-col{position:absolute;top:46px}
.footer-col h4{font-size:15px;font-weight:700;color:var(--teal);text-transform:uppercase;margin-bottom:12px}
.footer-col li{list-style:none;font-size:13px;font-weight:700;color:var(--white);line-height:21px;text-transform:uppercase}
.contact-line{display:flex;gap:10px;align-items:flex-start;font-size:13px;font-weight:700;color:var(--white);margin-bottom:16px;line-height:18px;text-transform:uppercase}
.contact-line.mail{text-transform:none}
.follow-line{display:flex;gap:10px;align-items:center;font-size:14px;font-weight:700;color:var(--white);margin-bottom:14px;text-transform:uppercase}
.follow-line span{width:22px;height:22px;border-radius:50%;background:var(--teal)}
.footer-brand{right:70px;top:130px;font-size:28px;font-weight:600;color:var(--navy)}
.copyright{height:37px;text-align:center;font-size:10px;color:var(--grey-text);padding-top:12px;text-transform:uppercase}
</style>
</head>
<body>

<header class="site-header">
  <div class="abs header-address">
    <svg width="22" height="32" viewBox="0 0 22 32"><path d="M11 0C4.9 0 0 4.9 0 11c0 8 11 21 11 21s11-13 11-21C22 4.9 17.1 0 11 0z" fill="#1d5a9c"/><circle cx="11" cy="11" r="4.5" fill="#fff"/></svg>
    <p>48 Meadowlark Lane<br>Chesterfield, MO 63017</p>
  </div>
  <div class="abs brand">Velantra Facial Surgery</div>
  <div class="abs header-phone">
    <svg width="40" height="40" viewBox="0 0 40 40"><circle cx="20" cy="20" r="18" fill="none" stroke="#2c3440" stroke-width="2.5"/><path d="M14 11c1-1 2.5-1 3 .5l1.5 3.5c.4 1-.2 2-1 2.5l-1 .7c1 2.5 3 4.5 5.3 5.5l.8-1c.6-.8 1.6-1.2 2.5-.8l3.4 1.6c1.4.6 1.4 2 .4 3l-1.7 1.7C23 31 10 18 14 11z" fill="#2c3440"/></svg>
    <div><small>CALL FOR APPOINTMENT</small><strong>800-555-0142</strong></div>
  </div>
</header>

<nav class="main-nav">
  <a class="active">Home</a>
  <a>Facial Procedures</a>
  <a>Office/Nonsurgical Procedures</a>
  <a>Practice</a>
  <a>Out of Town Patient</a>
  <a>Gallery</a>
  <a>What's New</a>
  <a>Velantra Med Spa</a>
  <a>Contact</a>
</nav>

<section class="hero">
  <div class="ph hero-photo" role="img" aria-label="Close-up portrait photograph of a woman, background for the surgery center tour video"></div>
  <div class="abs hero-title">Tour of the Surgery Center</div>
  <div class="abs hero-sub">See footage of the state of the art facility</div>
  <svg class="abs play" width="140" height="140" viewBox="0 0 140 140"><circle cx="70" cy="70" r="68" fill="rgba(255,255,255,.45)"/><path d="M56 44 L98 70 L56 96z" fill="#fff"/></svg>
  <div class="abs hero-strip"><span></span></div>
</section>

<section class="welcome">
  <h1>Welcome to Velantra Facial Surgery</h1>
  <p class="lorem">Lorem ipsum dolor sit amet, consectetuer adipiscing elit, sed diam nonummy nibh euismod tincidunt ut laoreet dolore magna aliquam erat volutpat. Ut wisi enim ad minim veniam, quis nostrud exerci tation ullamcorper suscipit lobortis nisl ut aliquip ex ea commodo.</p>
</section>

<section class="facial">
  <div class="ph facial-photo" role="img" aria-label="Photograph of a woman touching her face"></div>
  <div class="abs section-title">Facial <span class="accent">Procedures</span></div>
  <p class="abs lorem">Lorem ipsum dolor sit amet, consectetuer adipiscing elit, sed diam nonummy nibh euismod tincidunt ut laoreet dolore magna aliquam erat volutpat. Ut wisi enim ad minim veniam, quis nostrud exerci tation.</p>
  <div class="abs arrow" style="left:398px">&#8249;</div>
  <div class="card" style="left:425px">
    <div class="img" role="img" aria-label="Photograph of a microneedling treatment" style="background:linear-gradient(135deg,#d8b8a4,#a57a66)"></div>
    <div class="label">Microneedling<span class="plus">+</span></div>
  </div>
  <div class="card" style="left:768px">
    <div class="img" role="img" aria-label="Photograph of an ultrasound lift treatment device on skin" style="background:linear-gradient(135deg,#9fb6c2,#d4c0b2)"></div>
    <div class="label">Ultrasound Lift<span class="plus">+</span></div>
  </div>
  <div class="abs arrow" style="left:1115px">&#8250;</div>
</section>

<section class="office">
  <div class="abs section-title">Office/Non <span class="accent">Surgical Procedures</span></div>
  <p class="abs lorem">Lorem ipsum dolor sit amet, consectetuer adipiscing elit, sed diam nonummy nibh euismod tincidunt ut laoreet dolore magna aliquam erat volutpat. Ut wisi enim ad minim veniam, quis nostrud exerci tation ullamcorper suscipit lobortis nisl ut aliquip ex ea commodo consequat. Duis autem vel eum iriure dolor in hendrerit in vulputate velit esse molestie consequat, vel illum dolore eu feugiat nulla facilisis at vero eros et accumsan et iusto odio dignissim qui blandit praesent luptatum zzril delenit augue duis dolore te feugait nulla facilisi.</p>
  <div class="abs arrow" style="left:58px">&#8249;</div>
  <div class="card" style="left:98px">
    <div class="img" role="img" aria-label="Photograph of a fractional laser facial treatment" style="background:linear-gradient(135deg,#caa08a,#7d5b4c)"></div>
    <div class="label">Fractional Laser<span class="plus">+</span></div>
  </div>
  <div class="card" style="left:441px">
    <div class="img" role="img" aria-label="Photograph of a melasma peel treatment" style="background:linear-gradient(135deg,#e5cbb9,#b58b76)"></div>
    <div class="label">Melasma Peel<span class="plus">+</span></div>
  </div>
  <div class="card" style="left:784px">
    <div class="img" role="img" aria-label="Photograph of a dermaplaning treatment" style="background:linear-gradient(135deg,#ecd6c6,#c49e88)"></div>
    <div class="label">Dermaplaning<span class="plus">+</span></div>
  </div>
  <div class="abs arrow" style="left:1132px">&#8250;</div>
</section>

<section class="about">
  <div class="ph doctor-photo" role="img" aria-label="Photograph of the surgeon in a white coat"></div>
  <div class="abs section-title about-title"><span class="accent">About</span> Dr. Julian Hartwell</div>
  <p class="abs lorem bio">Lorem ipsum dolor sit amet, consectetuer adipiscing elit, sed diam nonummy nibh euismod tincidunt ut laoreet dolore magna aliquam erat volutpat. Ut wisi enim ad minim veniam, quis nostrud exercitation ullamcorper suscipit lobortis nisl ut aliquip ex ea commodo conse quat. Duis autem vel eum iriure dolor in hendrerit in vulputate velit esse molestie consequat, vel illum dolore eu feugiat nulla facilisis at vero eros et accumsan et iusto odio dignissim.</p>
  <span class="btn more">Learn More</span>
  <div class="abs section-title team-title">Meet <span class="accent">The Team</span></div>
  <div class="member" style="left:493px">
    <div class="avatar" role="img" aria-label="Portrait photograph of team member Owen Harlow"></div>
    <h3>Owen Harlow</h3><p>Assistant</p>
  </div>
  <div class="member" style="left:733px">
    <div class="avatar" role="img" aria-label="Portrait photograph of team member Miles Carver"></div>
    <h3>Miles Carver</h3><p>Assistant</p>
  </div>
</section>

<div class="spacer"></div>

<section class="out-town">
  <div class="ph backdrop" role="img" aria-label="Faded photograph of the clinic building in blue tones"></div>
  <div class="abs section-title">Out of Town <span class="accent">Patient</span></div>
  <p class="abs lorem">Lorem ipsum dolor sit amet, consectetuer adipiscing elit, sed diam nonummy nibh euismod tincidunt ut laoreet dolore magna aliquam erat volutpat. Ut wisi enim ad minim veniam, quis nostrud exerci tation ullamcorper suscipit lobortis nisl ut aliquip ex ea commodo consequat. Duis autem vel eum iriure dolor in hendrerit in vulputate velit esse molestie consequat, vel illum dolore eu feugiat nulla facilisis at vero eros et accumsan et iusto odio dignissim qui blandit praesent luptatum zzril delenit augue duis dolore te feugait nulla facilisi.</p>
  <span class="btn">Learn More</span>
</section>

<section class="gallery">
  <div class="abs section-title">Photo <span class="accent">Gallery</span></div>
  <div class="abs filter">Facelift
    <svg width="12" height="8" viewBox="0 0 12 8"><path d="M0 0h12L6 8z" fill="#fff"/></svg>
  </div>
  <div class="abs gallery-grid">
    <div role="img" aria-label="Facelift photograph with surgical marking lines, woman's jaw and neck" style="background:linear-gradient(135deg,#e9d4c4,#c59f89)"></div>
    <div role="img" aria-label="Facelift photograph with surgical marking lines on the face" style="background:linear-gradient(135deg,#f1e0d3,#d2b09b)"></div>
    <div role="img" aria-label="Photograph of an injection treatment on the cheek" style="background:linear-gradient(135deg,#efe3d9,#cfae99)"></div>
    <div role="img" aria-label="Eyelid surgery photograph with marking lines" style="background:linear-gradient(135deg,#c8b6ad,#8e7468)"></div>
    <div role="img" aria-label="Close-up photograph of a face with contour markings" style="background:linear-gradient(135deg,#e6c6ae,#b58567)"></div>
    <div role="img" aria-label="Photograph of a face with lift markings along the cheek" style="background:linear-gradient(135deg,#ecd9cb,#c8a692)"></div>
  </div>
</section>

<section class="social">
  <div class="abs section-title">Latest from <span class="accent">Facefeed and Chirper</span></div>
  <div class="widget fb-widget">
    <div class="ph fb-cover" role="img" aria-label="Page cover photograph"></div>
    <div class="abs fb-name">Velantra Facial Surgery</div>
    <div class="abs fb-like"><span>Like Page</span><span>Book Now</span></div>
    <div class="abs fb-friends">Be the first of your friends to like this</div>
    <div class="abs fb-faces"><span></span><span></span><span></span><span></span><span></span><span></span><span></span><span></span><span></span><span></span></div>
    <div class="abs fb-post">
      <div class="who"><span></span>Velantra Facial Surgery</div>
      <p>Lorem ipsum dolor sit amet, consectetuer adipiscing elit, sed diam nonummy nibh euismod tincidunt ut laoreet dolore magna aliquam erat volutpat. Ut wisi enim ad minim veniam, quis nostrud exerci tation ullamcorper suscipit lobortis nisl ut aliquip ex ea commodo consequat. Duis autem vel eum iriure dolor in hendrerit.</p>
      <div class="thumb" role="img" aria-label="Post photograph"></div>
    </div>
  </div>
  <div class="widget tw-widget">
    <div class="abs tw-head"><b>Tweets</b><span><svg width="10" height="10" viewBox="0 0 10 10"><circle cx="5" cy="5" r="5" fill="#1cb5b8"/></svg>Follow @VelantraFacial</span></div>
    <div class="tweet" style="top:58px"><small>Sept 26, 2015</small><p>Lorem ipsum dolor sit amet, consectetuer adipiscing elit, sed diam nonummy nibh euismod.</p></div>
    <div class="tweet" style="top:128px"><small>Sept 24, 2015</small><p>Lorem ipsum dolor sit amet, consectetuer adipiscing elit, sed diam nonummy nibh euismod tincidunt ut laoreet dolore magna aliquam erat volutpat.</p></div>
    <div class="tweet" style="top:228px"><small>Sept 20, 2015</small><p>Lorem ipsum dolor sit amet, consectetuer adipiscing elit, sed diam nonummy nibh euismod tincidunt ut laoreet dolore magna.</p></div>
    <div class="tweet" style="top:318px"><small>Sept 18, 2015</small><p>Lorem ipsum dolor sit amet, consectetuer adipiscing elit.</p></div>
    <div class="abs tw-foot">Tweet to @VelantraFacial</div>
  </div>
</section>

<section class="testimonials">
  <div class="abs section-title">Testimonials</div>
  <div class="ph quote-avatar" role="img" aria-label="Portrait photograph of patient Renata M."></div>
  <svg class="abs bubble-tip" width="16" height="20" viewBox="0 0 16 20"><path d="M0 0 L16 10 L0 20z" fill="#fff"/></svg>
  <div class="abs quote-mark" style="left:280px;top:80px">&#8220;</div>
  <p class="abs lorem">Lorem ipsum dolor sit amet, consectetuer adipiscing elit, sed diam nonummy nibh euismod tincidunt ut laoreet dolore magna aliquam erat volutpat. Ut wisi enim ad minim veniam, quis nostrud exercitation ullamcorper suscipit lobortis nisl ut aliquip ex ea commodo consequat.</p>
  <div class="abs quote-mark" style="left:1050px;top:140px">&#8221;</div>
  <div class="abs name">Renata M.</div>
  <div class="abs dots"><span class="on"></span><span></span><span></span></div>
</section>

<section class="booking">
  <div class="abs section-title">Book an <span class="accent">Appointment</span></div>
  <div class="abs form">
    <div class="row"><div class="field">Name</div><div class="field">Phone Number</div></div>
    <div class="row"><div class="field">Email Address</div><div class="field">Treatment <span>&#9662;</span></div></div>
    <div class="row"><div class="field">Desired Date <span>&#9662;</span></div><div class="field">Desired Hour <span>&#9662;</span></div></div>
    <div class="row"><div class="field area">Message/Comment</div></div>
    <span class="btn">Submit</span>
  </div>
  <div class="ph map" role="img" aria-label="Street map showing the clinic location"></div>
</section>

<footer class="site-footer">
  <svg class="abs footer-white" width="420" height="313" viewBox="0 0 420 313"><path d="M420 0 L420 313 L70 313 L300 0z" fill="#fff"/></svg>
  <div class="footer-col" style="left:72px">
    <h4>Navigation</h4>
    <ul>
      <li>Home</li><li>Facial Procedures</li><li>Office/Nonsurgical Procedures</li><li>Practice</li><li>Out of Town Patient</li><li>Gallery</li><li>What's New</li><li>Velantra Med Spa</li><li>Contact</li>
    </ul>
  </div>
  <div class="footer-col" style="left:386px">
    <h4>Contact Info</h4>
    <div class="contact-line"><svg width="14" height="20" viewBox="0 0 22 32"><path d="M11 0C4.9 0 0 4.9 0 11c0 8 11 21 11 21s11-13 11-21C22 4.9 17.1 0 11 0z" fill="#1cb5b8"/><circle cx="11" cy="11" r="4.5" fill="#1d5a9c"/></svg><span>48 Meadowlark Lane<br>Chesterfield, MO 63017</span></div>
    <div class="contact-line"><svg width="16" height="16" viewBox="0 0 16 16"><path d="M3 1c.8-.8 2-.8 2.4.4l1 2.6c.3.8-.1 1.5-.7 1.9l-.7.5c.8 2 2.3 3.5 4.1 4.3l.6-.8c.5-.6 1.2-.9 1.9-.6l2.6 1.2c1 .5 1 1.5.3 2.2l-1.3 1.3C9.5 15.8-.3 6.5 3 1z" fill="#1cb5b8"/></svg><span>800-555-0188</span></div>
    <div class="contact-line mail"><svg width="18" height="14" viewBox="0 0 18 14"><rect width="18" height="14" rx="2" fill="#1cb5b8"/><path d="M1 2 L9 8 L17 2" fill="none" stroke="#1d5a9c" stroke-width="1.6"/></svg><span>info@velantrafacial.com</span></div>
  </div>
  <div class="footer-col" style="left:720px">
    <h4>Follow Us</h4>
    <div class="follow-line"><span></span>Facefeed</div>
    <div class="follow-line"><span></span>Chirper</div>
  </div>
  <div class="abs footer-brand">Velantra</div>
</footer>

<div class="copyright">&copy; 2015 Velantra Facial Surgery. All rights reserved.</div>

</body>
</html>
```